Simple, Professional and neat business card design for Vendralo Inc.

We're looking to re-vamp our business card design. We're a supplier of innovative feed ingredients for the North American animal agriculture industry. We are located in Lucknow, Ontario, Canada and our flagship product is a product that prevents milk fever in dairy cows when the calve, it is fed before calving and is very effective compared to other alternatives available on the market today.

Our company has Danish roots and we import all of our product from our Danish partner/manufacturer in Denmark. We like our design to embrace high professionalism while remaining neat and simple.

Target Market(s)

B2B, Feed Mills, Veterinary Clinics, Large integrators/producers,

Industry/Entity Type

Agribusiness

Contact Information for Business Card

We like the rounded corners because they make the card easy to sit in a wallet and not many use it so it makes the card stand out, just possibly something to take account for during the design.

As you can also see on the sliders below, looking for a that simple but proffesional scandinavian design.

Requirements
Nice to have
• Rounded corners
Should not have
• Too vibrant

```html
<!DOCTYPE html>
<html lang="en">
<head>
<meta charset="utf-8">
<title>Vendralo Inc. business card</title>
<link rel="stylesheet" href="https://fonts.googleapis.com/css2?family=Montserrat:wght@500;600;700;800&display=swap">
<style>
  :root {
    --brand-blue: #1b5aa8;
    --accent-line: #8fc3e8;
    --card-white: #ffffff;
    --backdrop: #d8dfe0;
  }
  * { box-sizing: border-box; margin: 0; padding: 0; }
  html, body { width: 1200px; height: 1200px; overflow: hidden; }
  body {
    background: var(--backdrop);
    font-family: "Montserrat", Arial, sans-serif;
    position: relative;
  }
  .card {
    position: absolute;
    left: 270px;
    width: 664px;
    height: 400px;
    border-radius: 30px;
    overflow: hidden;
  }
  /* Front */
  .card-front { top: 154px; background: var(--card-white); }
  .front-band {
    position: absolute; left: 0; right: 0; height: 46px;
    background: var(--brand-blue);
  }
  .front-band--top { top: 0; border-bottom: 6px solid var(--card-white); box-shadow: 0 6px 0 var(--accent-line); }
  .front-band--bottom { bottom: 0; height: 48px; box-shadow: 0 -6px 0 var(--card-white), 0 -10px 0 var(--accent-line); }
  .wordmark {
    position: absolute; left: 126px; top: 170px;
    display: flex; align-items: center; gap: 22px;
  }
  .wordmark-dot {
    width: 52px; height: 52px; border-radius: 50%;
    background: var(--brand-blue);
  }
  .wordmark-name {
    font-weight: 700; font-size: 38px; color: var(--brand-blue);
    letter-spacing: 0.5px; text-transform: uppercase;
  }
  /* Back */
  .card-back { top: 666px; height: 396px; background: var(--brand-blue); color: var(--card-white); }
  .holder-name {
    position: absolute; left: 44px; top: 54px;
    font-weight: 700; font-size: 31px; letter-spacing: 0.5px;
  }
  .contact-list {
    position: absolute; top: 196px; list-style: none;
    font-weight: 500; font-size: 20px;
  }
  .contact-list--left { left: 76px; }
  .contact-list--right { left: 394px; }
  .contact-item { display: flex; align-items: center; gap: 6px; height: 34px; }
  .contact-item--gap { margin-top: 8px; }
  .contact-icon { width: 18px; height: 18px; flex: none; }
  .address-band {
    position: absolute; left: 0; right: 0; top: 314px; height: 40px;
    background: var(--card-white); color: var(--brand-blue);
    display: flex; align-items: center; justify-content: center;
    font-weight: 500; font-size: 18px;
  }
</style>
</head>
<body>

<section class="card card-front" aria-label="Card front">
  <div class="front-band front-band--top"></div>
  <div class="wordmark">
    <span class="wordmark-dot"></span>
    <span class="wordmark-name">Vendralo Inc.</span>
  </div>
  <div class="front-band front-band--bottom"></div>
</section>

<section class="card card-back" aria-label="Card back">
  <h1 class="holder-name">Henrik Solberg</h1>

  <ul class="contact-list contact-list--left">
    <li class="contact-item">
      <svg class="contact-icon" viewBox="0 0 18 18"><rect x="5" y="1" width="8" height="16" rx="1.5" fill="none" stroke="#fff" stroke-width="1.6"/><circle cx="9" cy="14.3" r="0.9" fill="#fff"/></svg>
      519-555-0143
    </li>
    <li class="contact-item">
      <svg class="contact-icon" viewBox="0 0 18 18"><path d="M2 7c0-3 14-3 14 0v1.5h-4V6.5H6v2H2z" fill="#fff"/><rect x="4" y="9" width="10" height="6" rx="1" fill="#fff"/></svg>
      519-555-0178
    </li>
    <li class="contact-item contact-item--gap">
      <svg class="contact-icon" viewBox="0 0 18 18"><rect x="1.5" y="4" width="15" height="10" rx="1" fill="none" stroke="#fff" stroke-width="1.6"/><path d="M2 5l7 5 7-5" fill="none" stroke="#fff" stroke-width="1.6"/></svg>
      henrik@vendralo.com
    </li>
  </ul>

  <ul class="contact-list contact-list--right">
    <li class="contact-item">
      <svg class="contact-icon" viewBox="0 0 18 18"><path d="M6 2 L8 5.5 6.5 7 C7 9 9 11 11 11.5 L12.5 10 16 12 14.5 15.5 C9 16 2 9 2.5 3.5 Z" fill="#fff"/></svg>
      888-555-0192
    </li>
    <li class="contact-item">
      <svg class="contact-icon" viewBox="0 0 18 18"><rect x="5" y="2" width="8" height="5" fill="#fff"/><rect x="1.5" y="7" width="15" height="6" rx="1" fill="#fff"/><rect x="5" y="11" width="8" height="5" fill="#fff" stroke="#1b5aa8" stroke-width="1"/></svg>
      519-555-0126
    </li>
    <li class="contact-item contact-item--gap">
      <svg class="contact-icon" viewBox="0 0 18 18"><circle cx="9" cy="9" r="7" fill="none" stroke="#fff" stroke-width="1.5"/><ellipse cx="9" cy="9" rx="3" ry="7" fill="none" stroke="#fff" stroke-width="1.3"/><path d="M2 9h14M3.5 5h11M3.5 13h11" stroke="#fff" stroke-width="1.2"/></svg>
      www.vendralo.com
    </li>
  </ul>

  <p class="address-band">Box 472, Brackenford, Norland Canada R4T 5K1</p>
</section>

</body>
</html>
```